A Dedicated Thank You to my Dad

Proposed Dimensions: Approx. 20" x 30"

For Father's Day, I wrote a dedication to my Dad that encapsulates my gratitude for everything he does, and everything he is. His birthday is on August 3, but it is more important for me to transform this dedication into a meaningful and memorable gift than to meet any deadline. I would love an image that captures the relationship between a father and his son, accompanied by my words of thanks in some sort of font that is appropriate for the message (calligprahy? not sure about that).

I had actually posted the Thank You on Pixelmarrow as a public post, so anyone with an account can read it: https://www.pixelmarrow.example/photo.php?fbid=40872219360548813&set=a.318760942157.6650129.3908471&type=1&theater

Only the words starting with "Thank you ..." should be on the poster.

Target Market(s)

This is a personal gift for my Dad. He doesn't have the best of eyesight, so having the words in a really small font would not be particularly helpful. :-)

Requirements
Must have
• * Personable
* Warm
* Inviting
* Memorable
* Understated more favored over Loud
Should not have
• * An entire palette of colors
* Wacky colors or fonts

```html
<!DOCTYPE html>
<html lang="en">
<head>
<meta charset="utf-8">
<title>A Dedicated Thank You</title>
<link rel="stylesheet" href="https://fonts.googleapis.com/css2?family=Courgette&family=Cormorant+SC:wght@500;600&family=Great+Vibes&display=swap">
<style>
  :root {
    --navy-deep: #1d1a6c;
    --navy-panel: #211e76;
    --navy-side: #2f2b8c;
    --navy-side-light: #4a45ad;
    --ornament-tone: #5c58b8;
    --lavender-line: #9a95e0;
    --text-light: #f1eff9;
    --title-silver: #d4d2e0;
    --photo-mid: #5d5aa8;
    --photo-light: #8582c6;
  }
  * { margin: 0; padding: 0; box-sizing: border-box; }
  html, body { width: 800px; height: 1200px; overflow: hidden; background: var(--navy-deep); }
  .poster {
    position: relative;
    width: 800px;
    height: 1200px;
    overflow: hidden;
    background: var(--navy-side);
  }
  .side-band {
    position: absolute;
    top: 0;
    height: 1200px;
    background: linear-gradient(to right, var(--navy-side) 0%, var(--navy-side-light) 50%, var(--navy-side) 100%);
  }
  .side-band--left { left: 0; width: 124px; background: linear-gradient(to right, var(--navy-side-light) 0%, var(--navy-side) 70%, var(--navy-deep) 100%); }
  .side-band--right { right: 0; width: 129px; background: linear-gradient(to left, var(--navy-side-light) 0%, var(--navy-side) 70%, var(--navy-deep) 100%); }
  .side-ornament {
    position: absolute;
    top: 20px;
    left: 10px;
    right: 14px;
    height: 1160px;
    border-radius: 60px;
    background: radial-gradient(ellipse at 50% 48%, rgba(92, 88, 184, 0.85) 0%, rgba(92, 88, 184, 0.45) 45%, rgba(92, 88, 184, 0) 80%);
  }
  .center-panel {
    position: absolute;
    top: 0;
    left: 124px;
    width: 547px;
    height: 1200px;
    background: var(--navy-panel);
    border-left: 2px solid var(--lavender-line);
    border-right: 2px solid var(--lavender-line);
    box-shadow: 0 0 18px rgba(10, 8, 50, 0.7);
  }
  .title-flourish {
    position: absolute;
    top: 0;
    left: 50px;
    width: 447px;
    height: 256px;
    background: radial-gradient(ellipse at 50% 45%, rgba(212, 210, 224, 0.14) 0%, rgba(212, 210, 224, 0.05) 50%, rgba(33, 30, 118, 0) 75%);
  }
  .title {
    position: absolute;
    top: 30px;
    left: 0;
    width: 543px;
    text-align: center;
    font-family: "Great Vibes", cursive;
    font-weight: 400;
    color: var(--title-silver);
  }
  .title__thank { display: block; font-size: 104px; line-height: 104px; }
  .title__you { display: block; font-size: 76px; line-height: 62px; margin-left: 24px; }
  .dedication {
    position: absolute;
    left: 0;
    width: 543px;
    text-align: center;
    color: var(--text-light);
  }
  .dedication__lead {
    font-family: "Courgette", cursive;
    font-size: 21px;
    line-height: 22px;
  }
  .dedication__rest {
    font-family: "Cormorant SC", serif;
    font-weight: 600;
    font-size: 15px;
    line-height: 17px;
    letter-spacing: 0.2px;
  }
  .father-son-photo {
    position: absolute;
    left: 0;
    bottom: 0;
    width: 543px;
    height: 345px;
    background: linear-gradient(to bottom, rgba(93, 90, 168, 0) 0%, rgba(93, 90, 168, 0.6) 22%, var(--photo-mid) 45%, var(--photo-light) 100%);
  }
</style>
</head>
<body>
<main class="poster">
  <div class="side-band side-band--left">
    <div class="side-ornament" role="img" aria-label="Ornamental floral damask pattern in soft violet"></div>
  </div>
  <div class="side-band side-band--right">
    <div class="side-ornament" role="img" aria-label="Ornamental floral damask pattern in soft violet"></div>
  </div>

  <section class="center-panel">
    <div class="title-flourish" role="img" aria-label="Silver flourishing swirls and small stars around the title"></div>
    <h1 class="title"><span class="title__thank">Thank</span><span class="title__you">You</span></h1>

    <div class="dedication" style="top:272px">
      <p class="dedication__lead">Thank You For Welcoming</p>
      <p class="dedication__rest">More People To Stay With Us Than I Can Count.</p>
    </div>
    <div class="dedication" style="top:324px">
      <p class="dedication__lead">Thank You For My Dry Sense Of Humor.</p>
      <p class="dedication__rest">I Cherish It.</p>
    </div>
    <div class="dedication" style="top:375px">
      <p class="dedication__lead">Thank You For Never Giving Up</p>
      <p class="dedication__rest">On Trying To Convince Me<br>That Imperfection Is Not A Failure.</p>
    </div>
    <div class="dedication" style="top:443px">
      <p class="dedication__lead">Thank You For Teaching Me</p>
      <p class="dedication__rest">To Try To Find The Good In Everyone.</p>
    </div>
    <div class="dedication" style="top:495px">
      <p class="dedication__lead">Thank You For Showing Me</p>
      <p class="dedication__rest">That There Is Peace To Be Found In Stillness And Quiet.</p>
    </div>
    <div class="dedication" style="top:546px">
      <p class="dedication__lead">Thank You For Demonstrating The Fun</p>
      <p class="dedication__rest">That Can Be Had And The Truths<br>That Can Be Gleaned From Debate.</p>
    </div>
    <div class="dedication" style="top:616px">
      <p class="dedication__lead">Thank You For Accepting Me For Who I Am,</p>
      <p class="dedication__rest">No Matter Who I Love, And For Helping Me To Accept Myself.</p>
    </div>
    <div class="dedication" style="top:667px">
      <p class="dedication__lead">Thank You For Doing Whatever You Can To Help</p>
      <p class="dedication__rest">Whoever You Can, Whether Friend, Family Or Stranger.</p>
    </div>
    <div class="dedication" style="top:719px">
      <p class="dedication__lead">Thank You For Trusting Me Enough</p>
      <p class="dedication__rest">To Let Your Guard Down To Let Me Know<br>How You Are Truly Doing.</p>
    </div>
    <div class="dedication" style="top:787px">
      <p class="dedication__lead">Thank You For Insisting, Year After Year,</p>
      <p class="dedication__rest">That Time With You Means More Than Any Gift<br>I Could Ever Purchase. That Is One Lesson, Amongst So Many,<br>That I Will Pass Down To Our Next Generation.</p>
    </div>

    <div class="father-son-photo" role="img" aria-label="Photograph of a smiling son and his father standing arm in arm in a doorway, tinted violet and fading into the panel"></div>
  </section>
</main>
</body>
</html>
```